Korvell Plant Services

We are a heavy diesel mechanical business with additional air con certificates, remapping engine rebuilt

Contact Information for Business Card

Company Name, Director Name, Managing Director, Contact details, email and website

Font styles to use
Serif
Script

```html
<!DOCTYPE html>
<html lang="en">
<head>
<meta charset="utf-8">
<title>Korvell Plant Services – Business Card</title>
<link href="https://fonts.googleapis.com/css2?family=Libre+Baskerville:wght@400;700&family=Great+Vibes&display=swap" rel="stylesheet">
<style>
  :root{
    --navy:#2d2a78;
    --ink:#111111;
    --paper:#ffffff;
    --backdrop:#6b6d6e;
    --band-text:#d4d3f2;
  }
  *{margin:0;padding:0;box-sizing:border-box}
  html,body{width:1200px;height:780px;overflow:hidden}
  body{
    background:var(--backdrop);
    font-family:"Libre Baskerville",Georgia,serif;
    position:relative;
  }
  .card{
    position:absolute;
    top:240px;
    width:520px;
    height:300px;
    border-radius:26px;
    overflow:hidden;
    box-shadow:0 10px 24px rgba(0,0,0,.35);
  }
  .card--front{left:50px;background:var(--navy);display:flex;align-items:center;justify-content:center}
  .card--back{left:630px;background:var(--paper)}

  .brand{display:flex;align-items:center;gap:14px}
  .brand__dot{border-radius:50%;flex:none}
  .brand__name{font-family:"Libre Baskerville",Georgia,serif;font-weight:700;line-height:1.1;white-space:nowrap}

  .card--front .brand__dot{width:28px;height:28px;border:3px solid var(--paper)}
  .card--front .brand__name{color:var(--paper);font-size:28px}

  .card--back .brand{justify-content:center;margin-top:24px;gap:10px}
  .card--back .brand__dot{width:16px;height:16px;border:2px solid var(--navy)}
  .card--back .brand__name{color:var(--navy);font-size:20px}

  .contact{text-align:center;margin-top:14px;color:var(--ink)}
  .contact__name{font-size:17px;letter-spacing:.5px;line-height:1.2}
  .contact__first{color:var(--navy)}
  .contact__last{font-weight:700}
  .contact__role{font-family:"Great Vibes",cursive;font-size:22px;line-height:1.1;margin-top:2px}
  .contact__phone{font-size:16px;margin-top:6px}
  .contact__web{font-size:12px;margin-top:8px;line-height:1.45}

  .address-band{
    position:absolute;left:0;right:0;bottom:0;height:48px;
    background:var(--navy);color:var(--band-text);
    display:flex;align-items:center;justify-content:center;
    font-size:14px;letter-spacing:.3px;
  }
</style>
</head>
<body>
  <section class="card card--front" aria-label="Card front">
    <div class="brand">
      <span class="brand__dot"></span>
      <span class="brand__name">Korvell Plant Services</span>
    </div>
  </section>

  <section class="card card--back" aria-label="Card back">
    <div class="brand">
      <span class="brand__dot"></span>
      <span class="brand__name">Korvell Plant Services</span>
    </div>
    <div class="contact">
      <p class="contact__name"><span class="contact__first">DALE</span> <span class="contact__last">HENSLEY</span></p>
      <p class="contact__role">Managing Director</p>
      <p class="contact__phone">(615) 555-0142</p>
      <p class="contact__web">office@korvellplant.com<br>www.korvellplant.com</p>
    </div>
    <div class="address-band">48 Harlan St Nashville, TN 37204</div>
  </section>
</body>
</html>
```